Business card design for new, innovative company - BluePlinth

We are a new company looking for a business card design that is fun, different and quirky. Must use corporate colour green - CMYK C:55, M:0, Y:100, K:0, and corporate colour grey - C:0, M:0, Y: 0, K:70.

We have developed the first real time data application, in which people are able to profile the data of their existing customers in order to pull out more good fit clients to direct their marketing activities at.

Industry/Entity Type

Marketing

Requirements
Must have
• Logo, name, title, telephone number, fax number, email, website, address

```html
<!DOCTYPE html>
<html lang="en">
<head>
<meta charset="utf-8">
<title>BluePlinth business card</title>
<link href="https://fonts.googleapis.com/css2?family=Questrial&display=swap" rel="stylesheet">
<style>
  :root {
    --brand-green: #7dc142;
    --brand-grey: #6d6e70;
    --ink-dark: #2e2f31;
    --card-back: #3c3d3f;
    --card-back-band: #5a5b5d;
    --frame-grey: #8d8e90;
    --paper: #ffffff;
    --stage: #e9e9e7;
  }
  * { margin: 0; padding: 0; box-sizing: border-box; }
  html, body {
    width: 1200px; height: 576px; overflow: hidden;
    background: var(--stage);
    font-family: "Questrial", "Century Gothic", sans-serif;
  }
  .stage {
    position: relative; width: 1200px; height: 576px;
    display: flex; align-items: center; justify-content: center; gap: 60px;
  }
  .card {
    position: relative; width: 500px; height: 286px;
    border-radius: 22px; overflow: hidden;
    box-shadow: 0 8px 24px rgba(0,0,0,.18);
  }

  /* Back side */
  .card-back { background: var(--card-back); }
  .card-back .pattern-fill {
    position: absolute; inset: 0;
    background: linear-gradient(160deg, #48494b, var(--card-back));
  }
  .card-back .band {
    position: absolute; left: 0; right: 0; top: 96px; height: 110px;
    background: linear-gradient(180deg, var(--card-back-band), #4b4c4e);
  }
  .card-back .wordmark {
    position: absolute; left: 0; right: 0; top: 112px;
    text-align: center; font-size: 54px; letter-spacing: -1px;
    color: var(--brand-green);
  }
  .card-back .web {
    position: absolute; left: 0; right: 0; top: 182px;
    text-align: center; font-size: 13px; color: var(--paper);
  }

  /* Front side */
  .card-front {
    background: var(--frame-grey);
    padding: 12px;
  }
  .card-front .face {
    position: relative; width: 100%; height: 100%;
    background: var(--paper); border-radius: 14px;
  }
  .person-name {
    position: absolute; left: 26px; top: 22px;
    font-size: 22px; color: var(--brand-green);
  }
  .person-title {
    position: absolute; left: 26px; top: 50px;
    font-size: 15px; color: var(--ink-dark);
  }
  .contact {
    position: absolute; left: 26px; top: 100px;
    list-style: none; font-size: 12.5px; line-height: 17px; color: var(--brand-grey);
  }
  .contact li { display: flex; align-items: flex-start; gap: 8px; }
  .contact svg { width: 11px; height: 11px; margin-top: 3px; flex: none; }
  .contact .indent { padding-left: 19px; }
  .contact strong { font-weight: normal; color: var(--ink-dark); }
  .front-wordmark {
    position: absolute; right: 28px; top: 150px;
    font-size: 38px; letter-spacing: -1px; color: var(--brand-green);
  }
</style>
</head>
<body>
<main class="stage">
  <section class="card card-back" aria-label="Card back">
    <div class="pattern-fill" role="img" aria-label="Subtle repeating tonal pattern on dark grey"></div>
    <div class="band"></div>
    <div class="wordmark">BluePlinth</div>
    <div class="web">www.blueplinth.com</div>
  </section>

  <section class="card card-front" aria-label="Card front">
    <div class="face">
      <div class="person-name">Dana Whitfield</div>
      <div class="person-title">CEO</div>
      <ul class="contact">
        <li>
          <svg viewBox="0 0 12 12"><path d="M6 0.5a4 4 0 0 1 4 4c0 3-4 7-4 7s-4-4-4-7a4 4 0 0 1 4-4z" fill="#7dc142"/><circle cx="6" cy="4.5" r="1.5" fill="#fff"/></svg>
          <span>22 Larkfield Road, Ely,</span>
        </li>
        <li class="indent">Cambridgeshire, CB7 4QT</li>
        <li>
          <svg viewBox="0 0 12 12"><rect x="3" y="0.5" width="6" height="11" rx="1.2" fill="#7dc142"/><rect x="4" y="2" width="4" height="7" fill="#fff"/></svg>
          <span>07700900457</span>
        </li>
        <li>
          <svg viewBox="0 0 12 12"><rect x="0.5" y="4" width="11" height="6" rx="1" fill="#7dc142"/><rect x="3" y="1" width="6" height="3.5" fill="#7dc142"/><rect x="3" y="7" width="6" height="4" fill="#fff" stroke="#7dc142"/></svg>
          <span>01632 960735</span>
        </li>
        <li>
          <svg viewBox="0 0 12 12"><rect x="0.5" y="2" width="11" height="8" rx="1" fill="#7dc142"/><path d="M1 2.5l5 4 5-4" fill="none" stroke="#fff" stroke-width="1"/></svg>
          <span>dana.whitfield@blueplinth.com</span>
        </li>
        <li>
          <svg viewBox="0 0 12 12"><circle cx="6" cy="6" r="5.5" fill="#7dc142"/><path d="M0.5 6h11M6 0.5c-3 3-3 8 0 11M6 0.5c3 3 3 8 0 11" fill="none" stroke="#fff" stroke-width=".8"/></svg>
          <span>www.<strong>blueplinth</strong>.com</span>
        </li>
      </ul>
      <div class="front-wordmark">BluePlinth</div>
    </div>
  </section>
</main>
</body>
</html>
```